Blue Ridge Haulers Website (quoting web application)

We need a website designed for our furniture moving company in Cape Town, South Africa.

I have attached some logos and images for you to use.

I have also attached the layout of the three pages we want designed (pdf file)

Dark blue is our colour.

The pictures of our trucks (uploaded) epitomise the design required.

Our old site (existing) is viewable here: blueridgehaulers.co.za

Target Market(s)

People moving house in Cape Town, South Africa.

Number of Pages Required

3 page

Font styles to use
Sans Serif

Colors
0255a3

Requirements
Must have
• Page design for the 3 pages in the pdf file.

```html
<!DOCTYPE html>
<html lang="en">
<head>
<meta charset="utf-8">
<title>Blue Ridge Haulers – Cape Town Movers</title>
<link href="https://fonts.googleapis.com/css2?family=Ubuntu:wght@400;500;700&family=Open+Sans:wght@400;600;700&family=Oswald:wght@500;600&display=swap" rel="stylesheet">
<style>
:root{
  --navy:#0b2a8c;
  --brand:#0255a3;
  --nav:#1747b8;
  --yellow:#f2b705;
  --red:#e0322c;
  --ink:#1d1d1d;
  --grey:#8a8a8a;
  --paper:#f1efef;
  --beige:#f5dfb4;
  --footer:#222222;
  --white:#ffffff;
}
*{box-sizing:border-box;margin:0;padding:0}
html,body{width:1200px;height:4196px;overflow:hidden}
body{position:relative;background:var(--white);font-family:"Open Sans",sans-serif;color:var(--ink)}
section,header,footer{position:absolute;left:0;width:1200px}
.abs{position:absolute}

/* header */
.site-header{top:0;height:173px}
.top-bar{position:absolute;top:0;left:0;width:1200px;height:112px;background:linear-gradient(180deg,#0d3fb0,#0a3198)}
.brand{position:absolute;left:120px;top:26px;display:flex;align-items:center;gap:14px}
.brand-mark{width:56px;height:56px;background:var(--white)}
.brand-name{font-family:"Ubuntu",sans-serif;font-weight:700;font-size:26px;color:var(--white);letter-spacing:1px;line-height:1}
.top-mail{position:absolute;right:292px;top:46px;font-size:14px;color:var(--white);text-align:right;white-space:nowrap}
.logout{position:absolute;left:938px;top:38px;width:136px;height:38px;background:var(--yellow);transform:skewX(-18deg);display:flex;align-items:center;justify-content:center}
.logout span{transform:skewX(18deg);font-size:14px;font-weight:700;color:var(--white)}
.main-nav{position:absolute;top:112px;left:0;width:1200px;height:61px;background:linear-gradient(180deg,#2354c9,#1440a8);display:flex;padding-left:120px}
.main-nav a{display:flex;align-items:center;padding:0 18px;font-size:14px;font-weight:600;color:var(--white);text-decoration:none}
.main-nav a.active{background:var(--yellow);padding:0 34px}

/* hero */
.hero{top:173px;height:479px}
.hero-photo{position:absolute;inset:0;background:linear-gradient(90deg,#3a3f46 0%,#50555b 45%,#2b2e33 100%)}
.hero-copy{position:absolute;left:690px;top:62px}
.hero-brand{font-family:"Ubuntu",sans-serif;font-weight:700;font-size:30px;color:var(--white);margin-left:60px;margin-bottom:30px}
.hero-title{font-family:"Oswald",sans-serif;font-weight:600;font-size:48px;line-height:1.12;color:var(--white);text-transform:uppercase}
.hero-title .hl{color:var(--yellow)}
.btn-quote{display:inline-block;margin-top:26px;background:var(--red);color:var(--white);font-weight:700;font-size:17px;padding:14px 28px}

/* section headings */
.heading-row{position:absolute;left:0;width:1200px;display:flex;align-items:center;justify-content:center;gap:22px}
.why{top:652px;height:425px;background:var(--paper)}
.why-title{top:60px;font-family:"Ubuntu",sans-serif;font-size:40px;color:var(--navy);font-weight:500}
.features{position:absolute;top:152px;left:93px;width:1014px;display:flex}
.feature{width:253px;text-align:center;padding:0 20px}
.feature-icon{width:78px;height:78px;border-radius:50%;background:var(--beige);margin:0 auto 26px;display:flex;align-items:center;justify-content:center}
.feature h3{font-family:"Ubuntu",sans-serif;font-size:16px;font-weight:700;text-transform:uppercase;margin-bottom:16px}
.feature p{font-size:12.5px;line-height:1.55;color:var(--grey)}

.quote{top:1077px;height:727px}
.quote-title{top:60px;gap:30px}
.quote-title .text{font-family:"Ubuntu",sans-serif;font-size:30px;font-weight:500;line-height:1.35;text-transform:uppercase;color:var(--ink);text-align:center}
.service-card{position:absolute;top:201px;width:230px;height:339px}
.service-photo{height:294px;background:linear-gradient(180deg,#c9b48f,#6d6250)}
.service-label{height:45px;background:var(--navy);color:var(--white);font-size:19px;display:flex;align-items:center;justify-content:center;text-transform:uppercase}

.stats{top:1804px;height:425px;background:linear-gradient(180deg,#26386e,#1e2e5d)}
.stats-title{position:absolute;top:60px;width:100%;text-align:center;font-family:"Ubuntu",sans-serif;font-size:32px;color:var(--white);text-transform:uppercase}
.review-badge{position:absolute;background:var(--white)}
.stat-caption{position:absolute;color:var(--white);font-size:13px;font-weight:600}
.stat-number{position:absolute;color:var(--white);font-family:"Ubuntu",sans-serif;font-weight:700;font-size:50px}

.helpers{top:2229px;height:568px}
.helpers h2{position:absolute;top:64px;width:100%;text-align:center;font-family:"Ubuntu",sans-serif;font-weight:400;font-size:25px}
.helpers h2 .accent{color:var(--yellow)}
.helpers p{position:absolute;top:104px;width:100%;text-align:center;font-size:13px;color:#555}
.helpers-art{position:absolute;left:154px;top:162px;width:895px;height:294px;background:linear-gradient(180deg,#eef1f7,#c7d0e4)}

.special{top:2797px;height:467px;background:var(--navy)}
.special-title{top:84px;font-family:"Ubuntu",sans-serif;font-size:32px;color:var(--white);text-transform:uppercase;font-weight:500}
.special-item{position:absolute;top:228px;width:170px;margin-left:-85px;text-align:center;color:var(--white);font-size:21px}
.special-item svg{display:block;margin:0 auto 22px}

.reviews{top:3264px;height:548px}
.reviews h2{position:absolute;top:56px;width:100%;text-align:center;font-family:"Ubuntu",sans-serif;font-weight:400;font-size:35px;text-transform:uppercase}
.reviews .lead{position:absolute;top:110px;width:100%;text-align:center;font-size:14px;color:#444}
.testimonial{position:absolute;left:255px;width:388px;background:#dfe3ea;padding:18px 22px;font-size:13px;line-height:1.55;color:#4a4a4a;font-style:italic}
.testimonial b{display:block;font-style:normal;color:var(--ink);margin-top:4px}
.post-card{position:absolute;left:671px;top:171px;width:249px;height:327px;border:1px solid #ddd;background:var(--white);padding:14px;font-size:11px;color:#333}
.post-head{display:flex;gap:8px;align-items:center;margin-bottom:10px}
.post-avatar{width:28px;height:28px;border-radius:50%;background:#b9c2d6}
.post-name{font-weight:700;font-size:12px}
.post-media{margin-top:12px;height:100px;background:var(--white);border:1px solid #e3e3e3;display:flex;align-items:center;justify-content:center;font-family:"Ubuntu",sans-serif;font-weight:700;font-size:15px;color:var(--navy)}
.post-meta{margin-top:8px;color:#888;font-size:10px;line-height:1.4}

.site-footer{top:3812px;height:384px;background:var(--footer);color:var(--white)}
.footer-brand{position:absolute;left:112px;top:96px;display:flex;align-items:center;gap:10px}
.footer-brand .brand-mark{width:44px;height:44px;background:#bfbfbf}
.footer-brand .brand-name{font-size:19px;color:#e6e6e6;letter-spacing:0}
.footer-col{position:absolute;top:78px}
.footer-col h4{font-family:"Ubuntu",sans-serif;font-size:17px;font-weight:500;margin-bottom:18px;text-transform:uppercase}
.footer-col li{list-style:none;font-size:11.5px;line-height:2.5;text-transform:uppercase;color:#ddd}
.footer-col .line{font-size:12.5px;line-height:2.2;color:#ddd}
.socials{display:flex;gap:12px}
.socials span{width:32px;height:32px;border:1.5px solid #ddd;border-radius:50%}
</style>
</head>
<body>

<header class="site-header">
  <div class="top-bar">
    <div class="brand"><span class="brand-mark"></span><span class="brand-name">BLUE RIDGE HAULERS</span></div>
    <div class="top-mail">bookings@blueridgehaulers.co.za</div>
    <div class="logout"><span>LOGOUT</span></div>
  </div>
  <nav class="main-nav">
    <a class="active">HOME</a><a>SERVICES</a><a>WHY CHOOSE US</a><a>ARTICLES</a><a>CONTACT US</a>
  </nav>
</header>

<section class="hero">
  <div class="hero-photo" role="img" aria-label="Photo of a black removals truck parked on a Cape Town street"></div>
  <div class="hero-copy">
    <div class="hero-brand">BLUE RIDGE HAULERS</div>
    <div class="hero-title">Get a quote an book<br><span class="hl">you move with our</span><br>Cape Town movers</div>
    <div class="btn-quote">FREE INSTANT QUOTE</div>
  </div>
</section>

<section class="why">
  <h2 class="heading-row why-title">
    <svg width="36" height="26" viewBox="0 0 36 26"><g stroke="var(--navy)" stroke-width="3"><line x1="0" y1="4" x2="36" y2="4"/><line x1="8" y1="12" x2="36" y2="12"/><line x1="16" y1="20" x2="36" y2="20"/></g></svg>
    <span>Why choose us?</span>
    <svg width="36" height="26" viewBox="0 0 36 26"><g stroke="var(--navy)" stroke-width="3"><line x1="0" y1="4" x2="36" y2="4"/><line x1="0" y1="12" x2="28" y2="12"/><line x1="0" y1="20" x2="20" y2="20"/></g></svg>
  </h2>
  <div class="features">
    <div class="feature">
      <div class="feature-icon"><svg width="40" height="40" viewBox="0 0 40 40" fill="none" stroke="#222" stroke-width="2"><path d="M4 20a16 14 0 0 1 32 0z"/><path d="M20 20v12a3 3 0 0 1-6 0"/></svg></div>
      <h3>Free insurance</h3>
      <p>We will fix or replace any furniture damaged during your Cape Town furniture removal</p>
    </div>
    <div class="feature">
      <div class="feature-icon"><svg width="40" height="40" viewBox="0 0 40 40" fill="none" stroke="#222" stroke-width="2"><path d="M5 20 20 7l15 13"/><path d="M10 17v16h20V17"/><rect x="17" y="24" width="6" height="9"/></svg></div>
      <h3>Professional &amp; friendly</h3>
      <p>We will fix or replace any furniture damaged during your Cape Town furniture removal</p>
    </div>
    <div class="feature">
      <div class="feature-icon"><svg width="40" height="40" viewBox="0 0 40 40" fill="none" stroke="#222" stroke-width="2"><path d="M20 5l4.5 9.5 10.5 1.3-7.7 7.2 2 10.3L20 28.2 10.7 33.3l2-10.3L5 15.8l10.5-1.3z"/></svg></div>
      <h3>Special services</h3>
      <p>We will fix or replace any furniture damaged during your Cape Town furniture removal</p>
    </div>
    <div class="feature">
      <div class="feature-icon"><svg width="40" height="40" viewBox="0 0 40 40" fill="none" stroke="#222" stroke-width="2"><circle cx="21" cy="21" r="14"/><path d="M21 12v10l6 4"/><path d="M5 12l3 4 4-3"/></svg></div>
      <h3>We arrive on time</h3>
      <p>We will fix or replace any furniture damaged during your Cape Town furniture removal</p>
    </div>
  </div>
</section>

<section class="quote">
  <h2 class="heading-row quote-title">
    <svg width="56" height="40" viewBox="0 0 56 40"><g stroke="var(--navy)" stroke-width="3.5"><line x1="0" y1="6" x2="56" y2="6"/><line x1="14" y1="18" x2="56" y2="18"/><line x1="26" y1="30" x2="56" y2="30"/></g></svg>
    <span class="text">Get a quote and book your move<br>with our Cape Town movers</span>
    <svg width="56" height="40" viewBox="0 0 56 40"><g stroke="var(--navy)" stroke-width="3.5"><line x1="0" y1="6" x2="56" y2="6"/><line x1="0" y1="18" x2="42" y2="18"/><line x1="0" y1="30" x2="30" y2="30"/></g></svg>
  </h2>
  <div class="service-card" style="left:131px"><div class="service-photo" role="img" aria-label="Mover carrying a chair out of a house"></div><div class="service-label">Home move</div></div>
  <div class="service-card" style="left:375px"><div class="service-photo" role="img" aria-label="Movers lifting a cabinet in an office" style="background:linear-gradient(180deg,#9a9a9a,#3b3b3b)"></div><div class="service-label">Business move</div></div>
  <div class="service-card" style="left:618px"><div class="service-photo" role="img" aria-label="Movers wrapping furniture on a lawn for storage" style="background:linear-gradient(180deg,#7ea05e,#4b6a3a)"></div><div class="service-label">Storage</div></div>
  <div class="service-card" style="left:864px"><div class="service-photo" role="img" aria-label="Mover setting down a sofa in a living room" style="background:linear-gradient(180deg,#d7cbbb,#9d8d78)"></div><div class="service-label">Mini move</div></div>
</section>

<section class="stats" role="img" aria-label="Moving crew standing in front of a blue truck">
  <h2 class="stats-title">Furniture removals Cape Town</h2>
  <div class="review-badge" style="left:221px;top:192px;width:179px;height:56px"></div>
  <div class="stat-caption" style="left:212px;top:256px;font-size:12px">4.8 star average rating by clients</div>
  <svg class="abs" style="left:232px;top:276px" width="160" height="28" viewBox="0 0 160 28"><g fill="var(--yellow)"><path id="st" d="M14 2l3.5 7.5 8 1-6 5.5 1.6 8-7.1-4-7.1 4 1.6-8-6-5.5 8-1z"/><use href="#st" x="32"/><use href="#st" x="64"/><use href="#st" x="96"/><use href="#st" x="128"/></g></svg>
  <div class="stat-caption" style="left:480px;top:196px">Loads completed in Cape Town</div>
  <div class="stat-number" style="left:534px;top:220px">3380</div>
  <div class="review-badge" style="left:797px;top:188px;width:157px;height:48px"></div>
  <div class="stat-number" style="left:800px;top:232px;font-size:44px">200000</div>
</section>

<section class="helpers">
  <h2>Two strong guys, one <span class="accent">relia</span>ble truck</h2>
  <p>Your items are safely loaded by two strong Ridge helpers!</p>
  <div class="helpers-art" role="img" aria-label="Illustration of two movers beside a small truck and a house with furniture"></div>
</section>

<section class="special">
  <h2 class="heading-row special-title">
    <svg width="44" height="32" viewBox="0 0 44 32"><g stroke="#fff" stroke-width="3"><line x1="0" y1="5" x2="44" y2="5"/><line x1="10" y1="15" x2="44" y2="15"/><line x1="20" y1="25" x2="44" y2="25"/></g></svg>
    <span>We do all the special services</span>
    <svg width="44" height="32" viewBox="0 0 44 32"><g stroke="#fff" stroke-width="3"><line x1="0" y1="5" x2="44" y2="5"/><line x1="0" y1="15" x2="34" y2="15"/><line x1="0" y1="25" x2="24" y2="25"/></g></svg>
  </h2>
  <div class="special-item" style="left:199px"><svg width="64" height="64" viewBox="0 0 64 64" fill="none" stroke="#fff" stroke-width="2.5"><path d="M20 60V8M4 14h56M20 8l-12 6M20 8l30 6"/><path d="M50 14v16"/><rect x="44" y="30" width="12" height="8"/><path d="M12 60h16"/></svg>Hoisting</div>
  <div class="special-item" style="left:372px"><svg width="64" height="64" viewBox="0 0 64 64" fill="none" stroke="#fff" stroke-width="2.5"><path d="M8 20l24-12 24 12-24 12z"/><path d="M8 20v24l24 12 24-12V20"/><path d="M32 32v24"/></svg>Box packing</div>
  <div class="special-item" style="left:557px"><svg width="64" height="64" viewBox="0 0 64 64" fill="none" stroke="#fff" stroke-width="2.5"><path d="M18 14a10 10 0 1 1 0 20h22"/><path d="M18 14v30c0 6 4 10 10 10h26V34"/></svg>wrapping</div>
  <div class="special-item" style="left:738px"><svg width="64" height="64" viewBox="0 0 64 64" fill="none" stroke="#fff" stroke-width="2.5"><rect x="10" y="16" width="44" height="16"/><rect x="4" y="30" width="56" height="14"/><path d="M10 44v6M54 44v6"/></svg>Dismantling</div>
  <div class="special-item" style="left:920px"><svg width="64" height="64" viewBox="0 0 64 64" fill="none" stroke="#fff" stroke-width="2.5"><path d="M10 18l22-10 22 10v28L32 56 10 46z"/><path d="M10 18l22 10 22-10M32 28v28"/></svg>Box delivery</div>
</section>

<section class="reviews">
  <h2>Happy customers</h2>
  <p class="lead">We take pride in our service and ensure a smooth and hassle-free move with our friendly movers.</p>
  <div class="testimonial" style="top:171px">"I'd like to make another booking based on the fact that I always have such excellent service and find your employees to be extremely professional and capable. Many thanks!"<b>Marika.</b></div>
  <div class="testimonial" style="top:336px">"I'd like to make another booking based on the fact that I always have such excellent service and find your employees to be extremely professional and capable. Many thanks!"<b>Marika.</b></div>
  <div class="post-card">
    <div class="post-head"><span class="post-avatar"></span><div><div class="post-name">Lena Varga</div><div style="color:#888;font-size:10px">@lena_varga</div></div></div>
    <div>Just used Blue Ridge Haulers for a mini move, the best guys, would gladly recommend them to friends.</div>
    <div class="post-meta">10:14 PM · Apr 8, 2018</div>
    <div class="post-media">BLUE RIDGE HAULERS</div>
    <div class="post-meta"><b style="color:#333">Blue Ridge Haulers – Cape Town Movers</b><br>Get a quote for your Cape Town furniture move<br>blueridgehaulers.co.za</div>
  </div>
</section>

<footer class="site-footer">
  <div class="footer-brand"><span class="brand-mark"></span><span class="brand-name">BLUE RIDGE HAULERS</span></div>
  <div class="footer-col" style="left:425px">
    <h4>Link</h4>
    <ul><li>Home</li><li>Services</li><li>Why choose us</li><li>Articles</li><li>Contact us</li></ul>
  </div>
  <div class="footer-col" style="left:585px">
    <h4>Contact</h4>
    <div class="line">GENERAL ENQUIRIES</div>
    <div class="line">bookings@blueridgehaulers.co.za</div>
    <div class="line">CALL US (NO QUOTES ON THE PHONE)</div>
    <div class="line">(021) 555 0188</div>
  </div>
  <div class="footer-col" style="left:861px">
    <h4>Follow us</h4>
    <div class="socials"><span></span><span></span><span></span><span></span></div>
  </div>
</footer>

</body>
</html>
```